Sidewalk Sign of store contents

I need a refresh on our current outdoor sandwhich board. We are getting vinyl done up and making a new A- frame sandwhich board. I want vinyl to be all in black with our logo on the top. I find this one attached a bit dated so need a more simple modern design with the logo at the top.

The vinyl will have to have all the words that are on the uploaded file plus the logo at the top. Looking for a nicer more simple modern design.

Oh please do not include the QZMT at the top ...just the circle "Velvet Larder" logo

Hip toronto cocktail lovers

Retail

000000

• Logo at the top. Please check out our website to see our style.
• Must have all the things mentioned on the file I uploaded but with only the "velvet Larder" logo at the top.
• velvetlarderco.com
• This is an outdoor A frame sidewalk sign about 2 feet by 3 feet. It must be eye catching for walkers. Want something more in line with the logo branding.
• It would be nice to have a graphic of a cocktail coupe within the design:)

```html
<!DOCTYPE html>
<html lang="en">
<head>
<meta charset="utf-8">
<title>Velvet Larder – Sidewalk Sign</title>
<link rel="stylesheet" href="https://fonts.googleapis.com/css2?family=Barlow+Condensed:wght@600;700&display=swap">
<style>
  :root {
    --backdrop: #f4f4f4;
    --board: #3a393b;
    --blush: #f5b3c3;
    --ink: #ffffff;
  }
  * { margin: 0; padding: 0; box-sizing: border-box; }
  html, body {
    width: 1200px; height: 1200px; overflow: hidden;
    background: var(--backdrop);
  }
  .sign {
    position: absolute; left: 220px; top: 30px;
    width: 760px; height: 1140px;
    background: var(--board);
    font-family: "Barlow Condensed", "Arial Narrow", sans-serif;
    font-weight: 700; color: var(--ink);
    text-transform: uppercase; overflow: hidden;
  }
  .brand {
    position: absolute; left: 0; right: 0; top: 120px;
    display: flex; justify-content: center; align-items: center; gap: 22px;
    color: var(--blush); font-weight: 600;
    font-size: 72px; text-transform: none; letter-spacing: 1px;
  }
  .brand-dot {
    width: 26px; height: 26px; border-radius: 50%;
    background: var(--blush);
  }
  .intro {
    position: absolute; left: 0; right: 0; top: 330px;
    text-align: center; line-height: 1.15;
  }
  .intro .line-lead { font-size: 52px; }
  .intro .line-sub { font-size: 44px; }
  .sep { color: var(--blush); margin: 0 10px; }
  .offerings {
    position: absolute; right: 50px; top: 470px;
    text-align: right; line-height: 1.12;
  }
  .offerings .mid { font-size: 46px; }
  .offerings .spaced { font-size: 46px; letter-spacing: 6px; }
  .offerings .big { font-size: 74px; line-height: 1.05; }
  .shop {
    position: absolute; right: 50px; top: 1010px;
    text-align: right; color: var(--blush);
    font-size: 38px; line-height: 1.1;
  }
  .coupe-area {
    position: absolute; left: 0; top: 560px;
    width: 250px; height: 580px;
    background: var(--blush);
  }
</style>
</head>
<body>
  <main class="sign">
    <div class="brand"><span class="brand-dot"></span>Velvet Larder</div>

    <div class="intro">
      <p class="line-lead">Garnishes<span class="sep">•</span>Syrup<span class="sep">•</span>Mixes</p>
      <p class="line-sub">Over 200 flavours of bitters</p>
    </div>

    <div class="coupe-area" role="img" aria-label="Pink cocktail coupe glass silhouette"></div>

    <div class="offerings">
      <p class="mid">New &amp; Vintage</p>
      <p class="spaced">Glassware</p>
      <p class="spaced">Accessories</p>
      <p class="big">Wine &amp; Beer</p>
      <p class="big">Bar Tools<span class="sep">•</span>Tiki</p>
      <p class="big">Cocktail Books</p>
    </div>

    <div class="shop">
      <p>Shop online</p>
      <p>velvetlarderco.com</p>
    </div>
  </main>
</body>
</html>
```